Fernmoor PTA Website Design

We are working with Fernmoor Elementary School PTA. They are a Parent Teacher Association that needs a new website design.

A Parent Teacher Association (PTA) is a volunteer organization that brings parents, teachers, and school staff together to support students and enhance their educational experience. PTAs organize fundraisers, sponsor school events, advocate for education policies, and foster stronger connections between families and schools.

Some sites to use for inspiration:

https://clubvane.com/demo/
https://nonprofits.fundrova.com/blogs/more-great-pta-websites-you-should-copy
https://www.qerbrix.com

Thank you for taking the time to consider designing a website for us. We are web developers based in Stockton and Los Angeles, CA, USA. Most of our projects go through the same process. Understanding this process may help you win a project with us. We custom-code all of our websites in-house. We don’t have any requirements as to what tools you use for your design, but we prefer Figma files. For any design that we label as four-stars, we send it to the client for review. The client picks the final design they want us to use. Once we complete this process, we will continue to show additional clients all the four-star sites and purchase them later. Your designs will have multiple chances to sell. For better chances of success, we ask that you follow these guidelines.

IMAGES:
If you use any images or icons in the design, we ask that you have a link to the asset so we can purchase the image/icon. Most of the designs we submit do not have the customer’s images on them unless they have some great images. Be creative; show us the feeling you are trying to portray with your image choices. Use any royalty-free site you choose. We subscribe to Vexiq and mainly use their images, but we can purchase images outside of Vexiq.

PLEASE NOTE: we will not submit designs to clients with watermarks on the images.

FONTS:
We ask that you identify the fonts used in the design. This can be done in a message if you want. We typically use Tarnel Fonts and Vexiq Fonts.

CONTENT:
We're always open to different content and ideas. We often submit designs with stock images so the client can see our vision. We typically take pictures after the website launch to use their images with our vision. Lorem Ipsum is fine for paragraphs, but we ask that you write the headers in correct English. We want to be able to show the vision and identify the sections of the website.

INSPIRATION:
We typically add a couple of links in the brief of websites we like to help you get started in your design.

REVISIONS:
We do not often ask for revisions of the designs unless we see something in the design that may not appeal to the client. If there are slight changes that we want to make, we do that in the development process.

FEEDBACK:
We rarely give feedback on designs during the design process. We are working on many website projects and do not have the time to provide feedback. We usually respond if your request is well thought out and asks specific questions, but a note asking “feedback, please” usually goes unanswered.

```html
<!DOCTYPE html>
<html lang="en">
<head>
<meta charset="utf-8">
<title>Fernmoor PTA</title>
<link href="https://fonts.googleapis.com/css2?family=Outfit:wght@300;400;500;600&display=swap" rel="stylesheet">
<style>
:root{
  --navy:#1f3b7c;
  --navy-dark:#1a3270;
  --ink:#2a2a2a;
  --muted:#3d3d3d;
  --white:#ffffff;
  --line:#d4d8e2;
}
*{box-sizing:border-box;margin:0;padding:0}
html,body{width:1200px;height:3523px;overflow:hidden;background:var(--white)}
body{position:relative;font-family:'Outfit',sans-serif;color:var(--ink);font-weight:300}
.abs{position:absolute}
a{color:inherit;text-decoration:none}

/* nav */
.nav{left:60px;top:34px;width:1084px;height:58px;background:var(--navy);border-radius:29px}
.nav-item{top:53px;color:var(--white);font-size:14.5px;font-weight:400;letter-spacing:.2px;white-space:nowrap}
.nav-item.active{font-weight:600;border-bottom:2px solid var(--white);padding-bottom:2px}
.nav-badge{left:542px;top:4px;width:116px;height:116px;border-radius:50%;background:var(--navy);display:flex;align-items:center;justify-content:center;color:var(--white);font-weight:600;font-size:17px}

/* hero */
.hero{left:59px;top:137px;width:1083px;height:484px;border-radius:22px;background:linear-gradient(120deg,#c9b89e 0%,#8e6e52 40%,#c59a6b 70%,#e7d8c4 100%)}

/* sidebar */
.sidebar{left:59px;top:665px;width:298px;height:858px;background:var(--navy);border-radius:20px}
.side-card{left:79px;width:254px;background:var(--white);border-radius:14px}
.pill{background:var(--navy);color:var(--white);border-radius:24px;font-size:14.5px;font-weight:400;display:flex;align-items:center;justify-content:center}
.side-text{font-size:14.5px;line-height:24px;color:var(--muted);word-break:break-all}
.contact-row{left:95px;display:flex;gap:8px;font-size:14.5px;line-height:24px;color:var(--muted);white-space:nowrap}
.contact-row svg{flex:none;margin-top:2px}
.map{left:101px;top:1334px;width:215px;height:120px;border-radius:6px;background:linear-gradient(135deg,#e8ecef,#d7e3d3)}

/* main */
.h-welcome{left:398px;top:700px;width:744px;text-align:center;font-size:40px;font-weight:500;line-height:47px;color:var(--ink)}
.p-center{text-align:center;font-size:14.5px;line-height:26.8px;color:var(--muted)}
.card{width:311px;height:370px;border-radius:14px;padding:18px 16px;text-align:center}
.card.dark{background:var(--navy);color:var(--white)}
.card.light{background:var(--white);border:1.5px solid var(--line);color:var(--muted)}
.card-img{width:234px;height:197px;margin:0 auto;border-radius:12px;border:1px solid var(--line)}
.card-title{font-size:21px;font-weight:400;margin-top:20px;line-height:26px}
.card.light .card-title{color:var(--ink)}
.card-text{font-size:14px;line-height:25px;margin-top:8px;height:75px;overflow:hidden}
.h-section{font-size:38px;font-weight:500;color:var(--ink)}
.p-body{font-size:14.5px;line-height:26.8px;color:var(--muted)}
.btn{background:var(--navy);color:var(--white);border-radius:24px;font-size:14.5px;font-weight:400;display:flex;align-items:center;justify-content:center}

.donate{left:399px;top:1825px;width:743px;height:651px;background:var(--navy);border-radius:20px}
.flyer{left:432px;top:1867px;width:678px;height:296px;border-radius:10px;background:linear-gradient(100deg,#d9effb 0%,#6fb5e4 45%,#2d6fc0 100%)}
.btn-outline{border:1.5px solid var(--white);color:var(--white);border-radius:24px;font-size:14.5px;display:flex;align-items:center;justify-content:center}

/* footer */
.footer{left:0;top:3105px;width:1200px;height:418px;background:var(--navy)}
.foot-logo{left:112px;top:3189px;width:159px;height:209px;display:flex;align-items:center;justify-content:center;color:var(--white);font-size:30px;font-weight:600}
.foot-h{top:3185px;color:var(--white);font-size:20px;font-weight:500}
.foot-rule{top:3230px;width:80px;height:2px;background:var(--white)}
.foot-link{color:var(--white);font-size:14.5px;font-weight:300;letter-spacing:.2px}
.social{left:847px;top:3377px;display:flex;gap:10px}
.social span{display:flex;align-items:center;gap:4px;color:var(--white);font-size:12px;font-weight:400}
.social span::before{content:"";width:10px;height:10px;border-radius:50%;background:var(--white)}
.foot-divider{left:0;top:3485px;width:1200px;height:1px;background:rgba(255,255,255,.55)}
.copyright{left:0;top:3496px;width:1200px;text-align:center;color:var(--white);font-size:13px;letter-spacing:.3px}
</style>
</head>
<body>

<!-- navigation -->
<div class="abs nav"></div>
<a class="abs nav-item active" style="left:103px">PTA AND YOU!</a>
<a class="abs nav-item" style="left:242px">FERNMOOR PTA STORE</a>
<a class="abs nav-item" style="left:440px">BLUE AND</a>
<div class="abs nav-badge">Fernmoor</div>
<a class="abs nav-item" style="left:672px">CONTACT US</a>
<a class="abs nav-item" style="left:803px">FERNMOOR PTA ON TOWNBOARD</a>

<!-- hero -->
<div class="abs hero" role="img" aria-label="Photo of smiling students eating lunch together at a classroom table"></div>

<!-- sidebar -->
<div class="abs sidebar"></div>
<div class="abs side-card" style="top:691px;height:358px"></div>
<div class="abs pill" style="left:94px;top:717px;width:225px;height:44px">Show Off your Lion Pride</div>
<div class="abs side-text" style="left:98px;top:786px;width:222px">Don't be caught unprepared!<br>Join PTA and make a difference.<br><br>Yearbooks are where it's at! Snap those photos of school events and fun days at Fernmoor then send them over to fernmoorlionsyearbook@quillpost.com!</div>

<div class="abs side-card" style="top:1078px;height:402px"></div>
<div class="abs pill" style="left:94px;top:1104px;width:225px;height:44px">Cotnact Us</div>
<div class="abs contact-row" style="top:1173px">
  <svg width="26" height="26" viewBox="0 0 26 26"><circle cx="13" cy="13" r="13" fill="#1f3b7c"/><rect x="7" y="9" width="12" height="8" rx="1" fill="none" stroke="#fff" stroke-width="1.5"/><path d="M7 9l6 5 6-5" fill="none" stroke="#fff" stroke-width="1.5"/></svg>
  <span>ptafernmoorlions@quillpost.com</span>
</div>
<div class="abs contact-row" style="top:1219px">
  <svg width="26" height="26" viewBox="0 0 26 26"><circle cx="13" cy="13" r="13" fill="#1f3b7c"/><path d="M9 7l3 0 1 3-2 1.5a8 8 0 003.5 3.5L16 13l3 1v3a1 1 0 01-1 1A11 11 0 018 8a1 1 0 011-1z" fill="#fff"/></svg>
  <span>(209)555-0147</span>
</div>
<div class="abs contact-row" style="top:1263px">
  <svg width="26" height="26" viewBox="0 0 26 26"><circle cx="13" cy="13" r="13" fill="#1f3b7c"/><path d="M13 6a5 5 0 015 5c0 4-5 9-5 9s-5-5-5-9a5 5 0 015-5z" fill="#fff"/><circle cx="13" cy="11" r="2" fill="#1f3b7c"/></svg>
  <span>1480 Alderbrook Place<br>Riverton, CA 95000</span>
</div>
<div class="abs map" role="img" aria-label="Street map showing the school location"></div>

<!-- welcome -->
<h1 class="abs h-welcome">Welcome to the<br>Fernmoor Elementary School PTA</h1>
<p class="abs p-center" style="left:405px;top:820px;width:730px">The Fernmoor Elementary School PTA is a volunteer organization made up of parents, teachers, and community members who work together to support our students and school. From sponsoring classroom supplies to hosting fun family events, we believe every contribution helps our Fernmoor Lions shine brighter. The Fernmoor Elementary School PTA unites parents, teachers, and staff to enrich every child's learning experience — from classrooms to community events.</p>

<!-- events carousel -->
<svg class="abs" style="left:397px;top:1172px" width="26" height="20" viewBox="0 0 26 20"><path d="M24 10H3M10 3L3 10l7 7" fill="none" stroke="#2a2a2a" stroke-width="2"/></svg>
<div class="abs card dark" style="left:446px;top:997px">
  <div class="card-img" role="img" aria-label="Fall carnival flyer with event date and activities" style="background:linear-gradient(180deg,#f6d98a,#f3a65a)"></div>
  <div class="card-title">2024 Fall Carnival</div>
  <div class="card-text">Join the fun and support the Fernmoor 6th Graders! Carnival games, tasty food, yummy treats</div>
</div>
<div class="abs card light" style="left:780px;top:997px">
  <div class="card-img" role="img" aria-label="Illustration of children having a picnic" style="background:linear-gradient(180deg,#ffffff,#f3e6d6)"></div>
  <div class="card-title">Spring Picnic</div>
  <div class="card-text">Friday, May 3 is our annual Spring Picnic supporting the next 6th grade class! Join us for a fantastic Starfarer-themed evening of fun</div>
</div>
<svg class="abs" style="left:1115px;top:1172px" width="26" height="20" viewBox="0 0 26 20"><path d="M2 10h21M16 3l7 7-7 7" fill="none" stroke="#2a2a2a" stroke-width="2"/></svg>

<!-- lion pride -->
<h2 class="abs h-section" style="left:398px;top:1438px">Show Off your Lion Pride</h2>
<p class="abs p-body" style="left:398px;top:1504px;width:740px">Don't be caught unprepared! Join PTA and make a difference.<br>Yearbooks are where it's at! &nbsp;Snap those photos of school events and fun days at Fernmoor then send them over to fernmoorlionsyearbook@quillpost.com!</p>
<p class="abs p-body" style="left:398px;top:1602px;width:740px">Also, you can't leave home without your Fernmoor Spirit Wear! Choose your style and size below then check out using your credit/debit card or PayQuill. We can't wait to see you show off your Lion Pride...even if it's only virtually right now!</p>
<div class="abs btn" style="left:398px;top:1706px;width:137px;height:45px">View Cart</div>

<!-- donate -->
<div class="abs donate"></div>
<div class="abs flyer" role="img" aria-label="Blue and White Take Flight auction save-the-date flyer"></div>
<h2 class="abs h-section" style="left:399px;top:2205px;width:743px;text-align:center;color:var(--white)">Donate Items or Dollars</h2>
<p class="abs p-center" style="left:432px;top:2273px;width:678px;color:var(--white)">What better way to get involved than to donate a basket for auction! &nbsp;Whether you donate it or you know businesses that can, supporting Fernmoor PTA is simple and easy - just print out the letter and form below and pass it around to your friends and local businesses.</p>
<div class="abs btn-outline" style="left:699px;top:2379px;width:142px;height:45px">Donate</div>

<!-- funded programs -->
<h2 class="abs h-section" style="left:398px;top:2546px;width:744px;text-align:center">PTA-Funded Programs</h2>
<svg class="abs" style="left:397px;top:2810px" width="26" height="20" viewBox="0 0 26 20"><path d="M24 10H3M10 3L3 10l7 7" fill="none" stroke="#2a2a2a" stroke-width="2"/></svg>
<div class="abs card dark" style="left:446px;top:2636px">
  <div class="card-img" role="img" aria-label="Illustrated stage with school assembly sign" style="background:linear-gradient(180deg,#f7e84a,#d8412f)"></div>
  <div class="card-title">Art Program</div>
  <div class="card-text">Through fundraising and generous donations, our PTA fully funds our entire art program - that means the teacher's full salary</div>
</div>
<div class="abs card light" style="left:780px;top:2636px">
  <div class="card-img" role="img" aria-label="Photo of colorful school and art supplies on a desk" style="background:linear-gradient(135deg,#e9b46a,#3f8fc8,#e45a5a)"></div>
  <div class="card-title">Teacher Supplies</div>
  <div class="card-text">With education budgets being tightened, we like to support our teachers in the big things as well as the little. That's why we like to help</div>
</div>
<svg class="abs" style="left:1115px;top:2810px" width="26" height="20" viewBox="0 0 26 20"><path d="M2 10h21M16 3l7 7-7 7" fill="none" stroke="#2a2a2a" stroke-width="2"/></svg>

<!-- footer -->
<footer class="abs footer"></footer>
<div class="abs foot-logo">Fernmoor</div>

<div class="abs foot-h" style="left:490px">QUICK LINKS</div>
<div class="abs foot-rule" style="left:490px"></div>
<a class="abs foot-link" style="left:490px;top:3260px">PTA AND YOU!</a>
<a class="abs foot-link" style="left:490px;top:3297px">FERNMOOR PTA STORE</a>
<a class="abs foot-link" style="left:490px;top:3334px">PTA-FUNDED PROGRAMS</a>
<a class="abs foot-link" style="left:490px;top:3371px">BLUE AND WHITE</a>

<div class="abs foot-h" style="left:847px">RESOURCES</div>
<div class="abs foot-rule" style="left:847px"></div>
<a class="abs foot-link" style="left:847px;top:3260px">CONTACT US</a>
<a class="abs foot-link" style="left:847px;top:3297px">FERNMOOR PTA ON TOWNBOARD</a>
<a class="abs foot-link" style="left:847px;top:3334px">FERNMOOR ELEMENTARY WEBSITE</a>
<div class="abs social"><span>Townboard</span><span>Clipvine</span><span>Snapfold</span></div>

<div class="abs foot-divider"></div>
<div class="abs copyright">COPYRIGHT © 2025 FERNMOOR PTA</div>

</body>
</html>
```